Postcard Design for QWAL-

We need a postcard designed that is similar to our current example with information but has a few changes for the season. It needs to be an oversized postcard that meets KRTB QWAL requirements.

In the section that says complete car care, I'd like to add a blurb that Summer is here! Make sure your Car is ready and your:
AC is cold
Cooling system is functioning properly
Tires and Alighment are vacation ready

Elsewhere on the card, we need to add that we offer a 3 year/36,000 warranty on parts and labor

We also need to add that we have a 5.0 Brivva Review Score and a 4.9 Lantor Vox score

Colors can change as can font as long as it is easy to read

```html
<!DOCTYPE html>
<html lang="en">
<head>
<meta charset="utf-8">
<title>Four Gear Auto Repair – Summer Postcard</title>
<link rel="stylesheet" href="https://fonts.googleapis.com/css2?family=Poppins:wght@400;600;800&family=Kanit:ital,wght@1,900&family=Mrs+Saint+Delafield&display=swap">
<style>
  :root {
    --green: #8bb949;
    --green-dark: #2d4a17;
    --blue: #5cc8f1;
    --grey: #e4e4e4;
    --backdrop: #acacac;
    --ink: #111111;
    --white: #ffffff;
    --steel-light: #e6e8ea;
    --steel-dark: #8c9196;
  }
  * { box-sizing: border-box; margin: 0; padding: 0; }
  html, body { width: 1058px; height: 1200px; overflow: hidden; }
  body { background: var(--backdrop); font-family: "Poppins", sans-serif; color: var(--ink); position: relative; }

  .postcard { position: absolute; left: 101px; width: 856px; height: 475px; background: var(--white); overflow: hidden; box-shadow: 0 4px 14px rgba(0,0,0,.25); }
  .postcard--front { top: 96px; }
  .postcard--back { top: 628px; }
  .abs { position: absolute; }

  /* front */
  .brand { left: 54px; top: 42px; display: flex; align-items: center; gap: 12px; }
  .brand__mark { width: 46px; height: 46px; border-radius: 50%; background: var(--ink); }
  .brand__name { font-weight: 600; font-size: 25px; line-height: 1.05; letter-spacing: .5px; color: var(--ink); }

  .perk-tag { left: 0; top: 0; width: 856px; height: 120px; }
  .perk-tag__text { left: 607px; top: 28px; font-size: 17px; line-height: 21px; color: var(--green-dark); }

  .wrench { height: 14px; border-radius: 7px; background: linear-gradient(180deg, var(--steel-light), var(--steel-dark)); }
  .wrench--top { left: 328px; top: 38px; width: 150px; transform: rotate(-37deg); }
  .wrench--mid { left: 530px; top: 144px; width: 175px; transform: rotate(34deg); }

  .script { font-family: "Mrs Saint Delafield", cursive; color: var(--green); white-space: nowrap; }
  .script--front { left: 300px; top: 82px; font-size: 58px; }
  .script--back { left: 44px; top: 96px; font-size: 66px; }

  .headline { font-family: "Kanit", sans-serif; font-style: italic; font-weight: 900; text-transform: uppercase; color: var(--ink); white-space: nowrap; transform-origin: left top; }
  .headline--summer { left: 50px; top: 146px; font-size: 68px; line-height: 57px; letter-spacing: 1px; transform: scaleX(1.38); }

  .lead { left: 51px; top: 272px; font-weight: 800; font-size: 23px; letter-spacing: -.2px; }
  .checklist { left: 51px; top: 312px; display: flex; gap: 22px; list-style: none; }
  .checklist__item { display: flex; gap: 7px; font-size: 15.5px; line-height: 19px; }
  .checklist__item svg { flex: none; margin-top: 2px; }

  .info-band { left: 0; top: 390px; width: 470px; height: 53px; background: var(--blue); border-bottom: 9px solid var(--grey); }
  .info-band__lines { left: 48px; top: 397px; font-size: 13.5px; line-height: 22px; }
  .info-band__lines p { display: flex; align-items: center; gap: 10px; }

  .photo { left: 0; top: 0; width: 856px; height: 475px; }
  .cta { left: 421px; top: 358px; width: 285px; height: 99px; }
  .cta__label { left: 478px; top: 368px; font-size: 35px; line-height: 40px; }
  .cta__phone { left: 462px; top: 410px; font-size: 24px; line-height: 28px; color: var(--white); }

  /* back */
  .mail-block { left: 0; top: 0; width: 350px; height: 88px; background: var(--grey); }
  .mail-band { left: 0; top: 18px; width: 297px; height: 45px; background: var(--blue); padding: 9px 0 0 36px; font-size: 12px; line-height: 15px; }
  .map-frame { left: 625px; top: 0; width: 231px; height: 263px; background: var(--grey); }
  .map { left: 632px; top: 5px; width: 224px; height: 254px; background: linear-gradient(160deg, #d3f5e2, #c9efdb); }
  .return-block { left: 551px; top: 254px; width: 305px; height: 221px; background: var(--grey); }
  .foot-strip { left: 0; top: 411px; width: 856px; height: 64px; background: var(--grey); }

  .headline--care { left: 42px; top: 166px; font-size: 92px; line-height: 72px; letter-spacing: 1px; transform: scaleX(1.2); }

  .services { left: 376px; top: 40px; width: 200px; }
  .services__title { font-weight: 800; font-size: 19.5px; line-height: 22px; text-transform: uppercase; }
  .services__copy { margin-top: 8px; font-size: 10.3px; line-height: 12.8px; width: 196px; }
  .perks { margin-top: 15px; list-style: none; }
  .perks__item { display: flex; align-items: center; gap: 10px; font-weight: 800; font-size: 11.5px; line-height: 15px; text-transform: uppercase; margin-bottom: 18px; margin-left: -3px; }
  .perks__icon { flex: none; width: 40px; height: 40px; border-radius: 50%; background: var(--green); display: grid; place-items: center; }

  .contact-band { left: 0; top: 332px; width: 518px; height: 62px; background: var(--grey); }
  .contact-band__inner { left: 0; top: 341px; width: 518px; height: 46px; background: var(--green); display: flex; align-items: center; gap: 36px; padding-left: 56px; color: var(--white); font-size: 20px; }
  .contact-band__inner span { display: flex; align-items: center; gap: 8px; }

  .assurances { left: 40px; top: 420px; list-style: none; font-size: 13px; line-height: 21px; font-weight: 600; }
  .assurances li { display: flex; align-items: center; gap: 8px; }
  .assurances__dot { width: 9px; height: 9px; border-radius: 50%; background: var(--green); flex: none; }
  .assurances strong { font-weight: 800; }

  .return-address { left: 572px; top: 335px; display: flex; gap: 6px; font-size: 10px; line-height: 15px; }
  .permit { left: 726px; top: 335px; border-left: 1px solid var(--ink); padding-left: 16px; height: 52px; font-size: 10px; line-height: 15px; text-transform: uppercase; }
</style>
</head>
<body>

<section class="postcard postcard--front" aria-label="Postcard front">
  <svg class="abs perk-tag" viewBox="0 0 856 120" aria-hidden="true">
    <polygon points="575,16 856,16 856,86 545,86" fill="var(--grey)"/>
    <polygon points="587,25 856,25 856,77 567,77" fill="var(--green)"/>
  </svg>
  <p class="abs perk-tag__text">Free vehicle pick up,<br>drop off, &amp; loaners</p>

  <div class="abs brand">
    <span class="brand__mark"></span>
    <p class="brand__name">FOUR GEAR<br>AUTO REPAIR</p>
  </div>

  <div class="abs wrench wrench--top" role="img" aria-label="Chrome combination wrench"></div>
  <p class="abs script script--front">High-quality</p>
  <div class="abs wrench wrench--mid" role="img" aria-label="Chrome combination wrench"></div>

  <h1 class="abs headline headline--summer">Summer is<br>here!</h1>
  <p class="abs lead">Make sure your Car is ready and your:</p>
  <ul class="abs checklist">
    <li class="checklist__item"><svg width="15" height="15" viewBox="0 0 16 16"><circle cx="8" cy="8" r="8" fill="var(--green)"/><path d="M4.5 8.3l2.3 2.2 4.7-4.8" stroke="#fff" stroke-width="1.8" fill="none"/></svg><span>AC is cold</span></li>
    <li class="checklist__item"><svg width="15" height="15" viewBox="0 0 16 16"><circle cx="8" cy="8" r="8" fill="var(--green)"/><path d="M4.5 8.3l2.3 2.2 4.7-4.8" stroke="#fff" stroke-width="1.8" fill="none"/></svg><span>Cooling system is<br>functioning properly</span></li>
    <li class="checklist__item"><svg width="15" height="15" viewBox="0 0 16 16"><circle cx="8" cy="8" r="8" fill="var(--green)"/><path d="M4.5 8.3l2.3 2.2 4.7-4.8" stroke="#fff" stroke-width="1.8" fill="none"/></svg><span>Tires and Alighment<br>are vacation ready</span></li>
  </ul>

  <div class="abs info-band"></div>
  <div class="abs info-band__lines">
    <p><svg width="12" height="13" viewBox="0 0 12 14"><path d="M6 1a3.5 3.5 0 0 0-3.5 3.5C2.5 7 6 10 6 10s3.5-3 3.5-5.5A3.5 3.5 0 0 0 6 1z" fill="none" stroke="var(--ink)" stroke-width="1.3"/><path d="M1 13h10" stroke="var(--ink)" stroke-width="1.3"/></svg>218 Larkfield Road, Unit C, Millbrook</p>
    <p><svg width="12" height="12" viewBox="0 0 12 12"><circle cx="6" cy="6" r="5" fill="none" stroke="var(--ink)" stroke-width="1.2"/><path d="M1 6h10M6 1c-2.5 3-2.5 7 0 10M6 1c2.5 3 2.5 7 0 10" fill="none" stroke="var(--ink)" stroke-width="1"/></svg>FourGearRepair.com</p>
  </div>

  <svg class="abs photo" viewBox="0 0 856 475">
    <polygon points="694,150 856,150 856,475 528,475" fill="var(--grey)"/>
    <defs><linearGradient id="shop" x1="0" y1="0" x2="0.4" y2="1"><stop offset="0" stop-color="#c9ccd0"/><stop offset=".45" stop-color="#7d8691"/><stop offset="1" stop-color="#2a2f38"/></linearGradient></defs>
    <polygon points="700,158 856,158 856,475 536,475" fill="url(#shop)" role="img" aria-label="Photo of a mechanic working under the bonnet of a white car in a workshop"/>
    <rect x="535" y="463" width="321" height="12" fill="#262b36"/>
  </svg>

  <svg class="abs cta" viewBox="0 0 285 99" aria-hidden="true">
    <path d="M60 0H272a10 10 0 0 1 9 14L238 88a20 20 0 0 1-17 11H14a10 10 0 0 1-9-14L43 11A20 20 0 0 1 60 0z" fill="var(--green)"/>
  </svg>
  <p class="abs headline cta__label">Call us</p>
  <p class="abs headline cta__phone">555-014-0288</p>
</section>

<section class="postcard postcard--back" aria-label="Postcard back">
  <div class="abs foot-strip"></div>
  <div class="abs mail-block"></div>
  <p class="abs mail-band">****************ECRWSS****QWAL<br>Local Postal Customer.</p>

  <div class="abs map-frame"></div>
  <div class="abs map" role="img" aria-label="Street map showing the shop location"></div>
  <div class="abs return-block"></div>

  <p class="abs script script--back">High-quality</p>
  <h2 class="abs headline headline--care">Car<br>care</h2>

  <div class="abs services">
    <h3 class="services__title">Including inspections and emissions</h3>
    <p class="services__copy">Don't trust your car to just any automotive repair shop. We have the reliable, experienced technicians to quickly diagnose what's wrong &amp; fix it right the first time-saving you time, headaches &amp; money.</p>
    <ul class="perks">
      <li class="perks__item"><span class="perks__icon"><svg width="22" height="22" viewBox="0 0 22 22"><circle cx="9" cy="9" r="6" fill="none" stroke="var(--ink)" stroke-width="3" stroke-dasharray="3 2"/><circle cx="9" cy="9" r="2" fill="var(--ink)"/><circle cx="16" cy="16" r="4" fill="var(--ink)"/></svg></span>Trust in a timely,<br>full-service<br>repair facility.</li>
      <li class="perks__item"><span class="perks__icon"><svg width="22" height="22" viewBox="0 0 22 22"><circle cx="11" cy="8" r="3" fill="var(--ink)"/><circle cx="5" cy="10" r="2.3" fill="var(--ink)"/><circle cx="17" cy="10" r="2.3" fill="var(--ink)"/><path d="M6 19a5 5 0 0 1 10 0zM1 19a4 4 0 0 1 6-3.5L6 19zM21 19a4 4 0 0 0-6-3.5L16 19z" fill="var(--ink)"/></svg></span>Enjoy<br>unparalleled<br>customer service</li>
    </ul>
  </div>

  <div class="abs contact-band"></div>
  <div class="abs contact-band__inner">
    <span><svg width="18" height="18" viewBox="0 0 18 18"><path d="M4 1l3 3-2 2.5a10 10 0 0 0 6.5 6.5L14 11l3 3-2.5 3C7 16.5 1.5 11 1 3.5z" fill="none" stroke="#fff" stroke-width="1.6"/></svg>555-014-0288</span>
    <span><svg width="20" height="20" viewBox="0 0 20 20"><circle cx="10" cy="10" r="8.5" fill="none" stroke="#fff" stroke-width="1.6"/><path d="M1.5 10h17M10 1.5c-4 4.5-4 12.5 0 17M10 1.5c4 4.5 4 12.5 0 17" fill="none" stroke="#fff" stroke-width="1.3"/></svg>FourGearRepair.com</span>
  </div>

  <ul class="abs assurances">
    <li><span class="assurances__dot"></span><span><strong>3 Year/36,000</strong> warranty on parts and labor</span></li>
    <li><span class="assurances__dot"></span><span><strong>5.0</strong> Brivva Review Score &nbsp;·&nbsp; <strong>4.9</strong> Lantor Vox Score</span></li>
  </ul>

  <div class="abs return-address">
    <svg width="8" height="11" viewBox="0 0 8 11"><path d="M4 0a4 4 0 0 0-4 4c0 3 4 7 4 7s4-4 4-7a4 4 0 0 0-4-4z" fill="var(--green)"/><circle cx="4" cy="4" r="1.4" fill="#fff"/></svg>
    <p>Four Gear Repair 218<br>Larkfield Road, Unit C<br>Millbrook, PA 17000</p>
  </div>
  <p class="abs permit">PRSRT STD<br>ECRWSS<br>U.S.Postage<br>Paid QWAL Retail</p>
</section>

</body>
</html>
```